Business card for dental office
Quillbrook Ridge Dental Care
Bright & Fun-filled
18 Larkspur Ln, Suite 310
Larkmont, NV 89777
quillbrookridgedentalcare@postmerro.com
quillbrookridgedentalcare.com
Please include website on business card but do not include email address.

```html
<!DOCTYPE html>
<html lang="en">
<head>
<meta charset="utf-8">
<title>Quillbrook Ridge Dental Care – Business Card</title>
<link href="https://fonts.googleapis.com/css2?family=Cinzel:wght@400;600&display=swap" rel="stylesheet">
<style>
  :root {
    --backdrop: #e9e7e4;
    --card: #ffffff;
    --ink-navy: #1f2b3d;
    --ink-blue: #2f9fd6;
    --ink-grey: #6b6f75;
    --rule: #c9cdd2;
    --shadow: rgba(0, 0, 0, 0.18);
  }
  * { margin: 0; padding: 0; box-sizing: border-box; }
  html, body {
    width: 1200px;
    height: 988px;
    overflow: hidden;
    background: var(--backdrop);
    font-family: "Cinzel", serif;
  }
  .canvas {
    width: 1200px;
    height: 988px;
    display: flex;
    flex-direction: column;
    align-items: center;
    justify-content: center;
    gap: 40px;
  }
  .card {
    width: 760px;
    height: 434px;
    background: var(--card);
    box-shadow: 0 8px 24px var(--shadow);
    position: relative;
  }
  .brand {
    position: absolute;
    left: 0;
    right: 0;
    display: flex;
    align-items: center;
    justify-content: center;
    gap: 14px;
  }
  .brand-dot {
    width: 22px;
    height: 22px;
    border-radius: 50%;
    background: var(--ink-blue);
    flex: none;
  }
  .brand-name {
    font-family: "Cinzel", serif;
    font-weight: 600;
    color: var(--ink-navy);
    letter-spacing: 1px;
    white-space: nowrap;
  }
  .card--back .brand { top: 180px; }
  .card--back .brand-name { font-size: 32px; }
  .card--front .brand { top: 70px; }
  .card--front .brand-name { font-size: 30px; }
  .practice-name {
    position: absolute;
    top: 168px;
    left: 0;
    right: 0;
    text-align: center;
    color: var(--ink-blue);
    font-size: 22px;
    letter-spacing: 1px;
  }
  .details {
    position: absolute;
    top: 228px;
    left: 0;
    right: 0;
    display: flex;
    justify-content: center;
    font-size: 16px;
    color: var(--ink-grey);
    line-height: 30px;
  }
  .address {
    text-align: right;
    padding-right: 18px;
    border-right: 1px solid var(--rule);
  }
  .contact {
    padding-left: 18px;
  }
  .contact-line {
    display: flex;
    align-items: center;
    gap: 10px;
    white-space: nowrap;
  }
  .icon {
    width: 18px;
    height: 18px;
    flex: none;
  }
</style>
</head>
<body>
<main class="canvas">
  <section class="card card--back" aria-label="Card back">
    <div class="brand">
      <span class="brand-dot"></span>
      <span class="brand-name">Quillbrook Ridge Dental Care</span>
    </div>
  </section>

  <section class="card card--front" aria-label="Card front">
    <div class="brand">
      <span class="brand-dot"></span>
      <span class="brand-name">Quillbrook Ridge Dental Care</span>
    </div>
    <p class="practice-name">Quillbrook Ridge Dental Care</p>
    <div class="details">
      <div class="address">
        <p>18 Larkspur Ln, Suite 310</p>
        <p>Larkmont, NV 89777</p>
      </div>
      <div class="contact">
        <p class="contact-line">
          <svg class="icon" viewBox="0 0 18 18" aria-hidden="true"><circle cx="9" cy="9" r="9" fill="#2f9fd6"/><path d="M6 4.5h2l.8 2.4-1.2.9a6 6 0 0 0 2.6 2.6l.9-1.2 2.4.8v2c0 .6-.5 1-1 1A8 8 0 0 1 5 5.5c0-.5.4-1 1-1z" fill="#fff"/></svg>
          775-555-0142
        </p>
        <p class="contact-line">
          <svg class="icon" viewBox="0 0 18 18" aria-hidden="true"><circle cx="9" cy="9" r="9" fill="#2f9fd6"/><rect x="5" y="7" width="8" height="5" fill="#fff"/><rect x="6.5" y="4.5" width="5" height="2.5" fill="#fff"/></svg>
          775-555-0187
        </p>
        <p class="contact-line">
          <svg class="icon" viewBox="0 0 18 18" aria-hidden="true"><circle cx="9" cy="9" r="9" fill="#2f9fd6"/><circle cx="9" cy="9" r="5" fill="none" stroke="#fff" stroke-width="1.2"/><path d="M4 9h10M9 4c-2.5 3-2.5 7 0 10M9 4c2.5 3 2.5 7 0 10" fill="none" stroke="#fff" stroke-width="1"/></svg>
          www.quillbrookridgedentalcare.com
        </p>
      </div>
    </div>
  </section>
</main>
</body>
</html>
```